minimalist website update needed, have wireframes

*Please start by making a design of the My Accounts page. If the overall template is correct, we can expand from there. Will give fast feedback.*

Financial services company (think online banking) is doing a complete website overhaul. We are going for the easiest, simplest possible user experience. We have the entire site mocked up in wireframes, but need a designer to make the final design drafts using photoshop or similar, then it needs to be coded into HTML/CSS.

*Current website*
https://brelvato.com/

*New website*
+ minimalist
+ white label of https://kestrapurse.org
+ skinning kestrapurse to be Brelvato branded, and targeted at beginners
+ wireframes for customized pages are attached
+ Landing page design is open. Please suggest one for bonus points!

Notes on the wireframes:
Open to rearranging the header content and menus.
Footer content is very rough. Just need to have a nice placeholder.
Needs social media icons
Needs language selector
My Accounts content is very rough. We want to use this area as a modular dashboard.
App Store is really just links to Bitcoin websites. These help users find useful and fun places to spend their money.

*Branding?*
As part of the process, our branding may need an update. Orange is currently our primary color, and it doesn't match well with the new, simplistic layout. We're willing to explore changes to the brand, if it works better with the new design.

Current visual identity guide is attached.
Updates

Project Deadline Extended
Reason: It seems for this many pages, it is better to leave more time. First we have to get the template right, then content elements, then HTML/CSS. I underestimated the complexity, forgive me for the modification.

Target Market(s)

People who make online purchases, or send money online.

Industry/Entity Type

Financial

Coding

Coded - Design and coding required

Number of Pages Required

5+ page

Requirements
Must have
• Pretty versions of the attached wireframes in HTML
Nice to have
• Landing page

```html
<!DOCTYPE html>
<html lang="en">
<head>
<meta charset="utf-8">
<title>Brelvato – Fund</title>
<link href="https://fonts.googleapis.com/css2?family=Open+Sans:wght@400;600&family=Ubuntu:wght@400;500;700&display=swap" rel="stylesheet">
<style>
:root{
  --green:#5bb394;
  --green-dark:#4ea585;
  --orange:#f8722c;
  --orange-edge:#e3621f;
  --sidebar:#454545;
  --sidebar-line:#525252;
  --text:#555;
  --muted:#666;
  --line:#d8d8d8;
  --row:#ececec;
}
*{box-sizing:border-box;margin:0;padding:0}
html,body{width:1200px;height:806px;overflow:hidden}
body{position:relative;font-family:'Open Sans',sans-serif;color:var(--text);background:#fff}
a{color:inherit;text-decoration:none}

.site-header{position:absolute;left:0;top:0;width:1200px;height:89px;background:#fff;border-bottom:1px solid #e2e2e2;box-shadow:0 1px 3px rgba(0,0,0,.06)}
.brand{position:absolute;left:18px;top:30px;display:flex;align-items:center;gap:10px}
.brand-dot{width:26px;height:26px;border-radius:50%;background:var(--orange)}
.brand-name{font-family:'Ubuntu',sans-serif;font-weight:700;font-size:19px;letter-spacing:3px;color:var(--orange)}
.user{position:absolute;left:257px;top:34px;display:flex;align-items:center;gap:8px;font-size:12px;color:var(--muted)}
.user-icon{width:27px;height:27px;border-radius:50%;background:var(--green);display:flex;align-items:center;justify-content:center}
.balance{position:absolute;left:403px;top:33px;width:144px;height:29px;border:1px solid #ccc;font-size:11px;color:var(--muted);padding:7px 11px}
.balance::after{content:"";position:absolute;right:10px;top:12px;border:4px solid transparent;border-top:5px solid #666}
.main-nav{position:absolute;left:580px;top:40px;font-size:12px;color:var(--muted)}
.main-nav a{position:absolute;white-space:nowrap}
.logout{position:absolute;left:913px;top:33px;width:90px;height:30px;background:var(--orange);border:1px solid var(--orange-edge);color:#fff;font-size:12px;text-align:center;line-height:28px}

.sidebar{position:absolute;left:0;top:90px;width:192px;height:447px;background:var(--sidebar)}
.side-item{height:47px;border-bottom:1px solid var(--sidebar-line);display:flex;align-items:center;gap:9px;padding-left:17px;font-size:12px;color:#bbb}
.side-item svg{width:12px;height:12px;fill:#aaa}
.side-item.active{background:var(--green);color:#fff;font-weight:600}
.side-item.active svg{fill:#fff}

.content{position:absolute;left:214px;top:118px;width:789px}
.panel-title{height:48px;border:1px solid #ddd;background:linear-gradient(#fff,#f1f1f1);padding:0 17px;display:flex;align-items:center;justify-content:space-between;font-size:17px;color:#444}
.help{width:24px;height:24px;border-radius:50%;background:var(--green);color:#fff;font-size:13px;text-align:center;line-height:24px}
.tabs{position:relative;margin-top:23px;height:32px;border-bottom:1px solid #ccc;font-size:13px;color:#444}
.tab{position:absolute;top:8px}
.tab.current{top:0;left:209px;width:186px;height:33px;border:1px solid #ccc;border-bottom:1px solid #fff;background:#fff;text-align:center;padding-top:8px}
.intro{margin:26px 0 0 18px;width:720px;font-size:11.3px;line-height:22px;color:#555}
.add-btn{display:block;margin:15px 0 0 18px;width:127px;height:35px;background:var(--orange);border:1px solid var(--orange-edge);color:#fff;font-size:11.5px;text-align:center;line-height:33px}
.accounts{margin:33px 0 0 16px;width:569px;border-collapse:collapse;font-size:11px}
.accounts th{background:var(--green);color:#fff;font-weight:400;height:39px;text-align:left;padding-left:22px;border-right:1px solid #7cc3a9}
.accounts td{background:var(--row);height:39px;padding-left:22px;color:#555;border:1px solid #d4d4d4}
.accounts .desc{position:relative}
.remove{position:absolute;right:8px;top:8px;width:70px;height:22px;background:var(--green);border:1px solid #4a9e81;border-radius:2px;color:#fff;font-size:11px;text-align:center;line-height:20px}

.footer{position:absolute;left:0;top:537px;width:1200px;height:209px;background:var(--green);font-family:'Ubuntu',sans-serif;color:#fff}
.col{position:absolute;top:38px}
.col h3{font-size:13.5px;font-weight:500;margin-bottom:13px}
.col li{list-style:none;font-size:11px;height:27px}
.col li::before{content:"›";margin-right:8px}
.signup p{font-size:11px}
.email-field{margin-top:16px;width:259px;height:32px;background:#fff;color:#555;font-size:11px;padding:9px 15px}
.subscribe{margin-top:13px;width:139px;height:34px;background:var(--sidebar);color:#fff;font-size:11px;text-align:center;line-height:34px;border-radius:2px}
.bottom-bar{position:absolute;left:0;top:746px;width:1200px;height:60px;background:var(--green-dark);font-family:'Ubuntu',sans-serif;color:#fff;font-size:11px}
.legal{position:absolute;left:56px;top:22px;word-spacing:1px}
.legal span{margin:0 14px}
.social{position:absolute;left:796px;top:16px;display:flex;gap:9px}
.social i{width:28px;height:28px;border-radius:50%;background:#fff;display:block}
</style>
</head>
<body>

<header class="site-header">
  <div class="brand"><span class="brand-dot"></span><span class="brand-name">BRELVATO</span></div>
  <div class="user">
    <span class="user-icon"><svg width="12" height="9" viewBox="0 0 12 9"><rect width="12" height="9" rx="1" fill="#fff"/><path d="M0 1l6 4 6-4" stroke="#5bb394" fill="none" stroke-width="1.2"/></svg></span>
    name@email.com
  </div>
  <div class="balance">US$11,05109</div>
  <nav class="main-nav">
    <a style="left:0">My Wallet</a>
    <a style="left:83px">Store</a>
    <a style="left:143px">Explorer</a>
    <a style="left:218px">About</a>
    <a style="left:281px">Status</a>
  </nav>
  <a class="logout">LOGOUT</a>
</header>

<aside class="sidebar">
  <div class="side-item"><svg viewBox="0 0 12 12"><path d="M1 0h10v12H1zM3 2v2h6V2zM3 6v1h1V6zm2.5 0v1h1V6zM8 6v1h1V6zM3 9v1h1V9zm2.5 0v1h1V9zM8 9v1h1V9z"/></svg>Accounts</div>
  <div class="side-item"><svg viewBox="0 0 12 12"><path d="M7 1l5 4-5 4V7C3 7 1 9 0 11c0-5 3-7 7-7z"/></svg>Send</div>
  <div class="side-item active"><svg viewBox="0 0 12 12"><path d="M0 2h12v8H0zm2 2v4h8V4zm4 .8a1.2 1.2 0 100 2.4 1.2 1.2 0 000-2.4z"/></svg>Fund</div>
  <div class="side-item"><svg viewBox="0 0 12 12"><path d="M5 0h2v5h2L6 8 3 5h2zM0 8h2v2h8V8h2v4H0z"/></svg>Convert</div>
  <div class="side-item"><svg viewBox="0 0 12 12"><circle cx="6" cy="6" r="6"/></svg>History</div>
  <div class="side-item"><svg viewBox="0 0 12 12"><path d="M5 0h2l.4 1.8 1.6.7 1.5-1 1.4 1.4-1 1.5.7 1.6L12 5v2l-1.8.4-.7 1.6 1 1.5-1.4 1.4-1.5-1-1.6.7L7 12H5l-.4-1.8-1.6-.7-1.5 1L.1 9.1l1-1.5-.7-1.6L0 7V5l1.8-.4.7-1.6-1-1.5L2.9.1l1.5 1 1.6-.7zM6 4a2 2 0 100 4 2 2 0 000-4z"/></svg>Settings</div>
</aside>

<main class="content">
  <div class="panel-title">Fund <span class="help">?</span></div>
  <div class="tabs">
    <span class="tab" style="left:29px">Deposit</span>
    <span class="tab" style="left:129px">Withdrew</span>
    <span class="tab current">Manage Linked Accounts</span>
  </div>
  <p class="intro">Lorem Ipsum es simplemente el texto de relleno de las imprentas y archivos de texto. Lorem Ipsum ha sido el texto de relleno estándar de las industrias desde el año 1500, cuando un impresor (N. del T. persona que se dedica a la imprenta) desconocido usó una galería de textos y los mezcló de tal manera que logró hacer un libro de textos especimen.</p>
  <a class="add-btn">ADD ACCOUNT</a>
  <table class="accounts">
    <tr><th style="width:175px">Account Number</th><th style="width:120px">Currency</th><th style="padding-left:17px">Discription (Same as account name)</th></tr>
    <tr><td>9120174900</td><td>USD</td><td class="desc" style="padding-left:18px;padding-top:4px">My name - USD<a class="remove">Remove</a></td></tr>
  </table>
</main>

<footer class="footer">
  <div class="col signup" style="left:57px">
    <h3>NEWSLETTER SIGNUP</h3>
    <p>Subscribe to our newsletter by entering your email</p>
    <div class="email-field">Enter your email id :</div>
    <div class="subscribe">SUBSCRIBE</div>
  </div>
  <div class="col" style="left:425px">
    <h3>BITCOIN WALLET</h3>
    <ul><li>Create your Wallet</li><li>Learn about Locks</li></ul>
  </div>
  <div class="col" style="left:639px">
    <h3>MERCHANT SERVICES</h3>
    <ul><li>Information</li><li>Send Invoices</li><li>API</li></ul>
  </div>
  <div class="col" style="left:862px">
    <h3>BRELVATO</h3>
    <ul><li>About Brelvato</li><li>Blog</li><li>Contact</li><li>Support</li></ul>
  </div>
</footer>
<div class="bottom-bar">
  <div class="legal">© 2012-2015 Brelvato.com. All rights reserved<span>/</span>Privacy Policy<span>/</span>Terms</div>
  <div class="social" aria-label="Social links"><i></i><i></i><i></i><i></i><i></i></div>
</div>

</body>
</html>
```